Web Design Project - Homepage mockup for media services company

Client would like a site much like this example below in terms of design and layout:

http://plumtide.net/

It's a media services company and the services they provide are:
-audio/video production
-graphic design
-social media
-web development
-apparel design

Their logo file is attached. I have also attached some of their service descriptions if that at all helps with things.

```html
<!DOCTYPE html>
<html lang="en">
<head>
<meta charset="utf-8">
<title>Norvane – Media Services</title>
<link href="https://fonts.googleapis.com/css2?family=Titillium+Web:wght@400;600&family=Open+Sans:wght@400;600&display=swap" rel="stylesheet">
<style>
:root{
  --sky-top:#6fb2ec;
  --sky-mid:#3a82d2;
  --hero-top:#3f86cf;
  --hero-bottom:#1d4f93;
  --navy:#11234b;
  --navy-deep:#0c1a3a;
  --nav-btn:#163c6e;
  --tab:#1f4f8a;
  --heading:#1d4f86;
  --sub:#1b2c44;
  --body:#4a4a4a;
  --muted:#777;
  --link:#a21d1d;
  --orange-a:#ffa21a;
  --orange-b:#f56d00;
  --footer:#f1f1f1;
  --footer-bar:#e1e1e1;
  --white:#ffffff;
}
*{margin:0;padding:0;box-sizing:border-box}
html,body{width:902px;height:1200px;overflow:hidden}
body{position:relative;background:var(--navy);font-family:"Open Sans",sans-serif;color:var(--body)}
.abs{position:absolute}

/* header */
.site-header{left:0;top:0;width:902px;height:108px;
  background:linear-gradient(180deg,var(--sky-top) 0%,var(--sky-mid) 55%,#9cc8ef 80%,#dcecf9 92%,#7fb2e2 100%);overflow:hidden}
.site-header svg{position:absolute;left:0;top:0}
.brand{left:84px;top:10px;display:flex;align-items:center;gap:8px}
.brand-mark{width:80px;height:80px;border-radius:50%;background:#1a1a1a;border:3px solid #d9d9d9}
.brand-name{font-family:"Titillium Web",sans-serif;font-weight:600;font-size:30px;color:var(--white)}
.main-nav{left:440px;top:48px;display:flex;gap:9px}
.main-nav a{display:block;height:26px;line-height:25px;text-align:center;color:var(--white);text-decoration:none;
  font-family:"Titillium Web",sans-serif;font-size:11px;background:var(--nav-btn);border:1px solid #6e9bd0;border-radius:6px;
  box-shadow:inset 0 1px 0 rgba(255,255,255,.25)}

/* hero */
.hero{left:0;top:108px;width:902px;height:280px;
  background:radial-gradient(ellipse 320px 240px at 420px 0,rgba(160,210,255,.55),rgba(160,210,255,0) 70%),
  linear-gradient(180deg,var(--hero-top),var(--hero-bottom))}
.hero-title{left:136px;top:50px;font-family:"Titillium Web",sans-serif;font-size:22px;color:var(--white)}
.hero-text{left:141px;top:86px;width:257px;font-size:10px;line-height:18px;color:#eaf3ff;text-align:justify}
.cta{left:243px;top:184px;width:127px;height:41px;border-radius:5px;
  background:linear-gradient(180deg,var(--orange-a),var(--orange-b));color:var(--white);
  font-family:"Titillium Web",sans-serif;font-size:13px;line-height:41px;text-align:center;box-shadow:0 2px 4px rgba(0,0,0,.3)}
.cta-reflection{left:243px;top:227px;width:127px;height:32px;border-radius:5px;
  background:linear-gradient(180deg,rgba(245,140,20,.55),rgba(245,140,20,0))}
.hero-art{left:480px;top:20px;width:264px;height:224px;border-radius:10px;
  background:radial-gradient(circle at 50% 55%,#9fc6e8,#4d7fb8 60%,rgba(60,110,180,0) 75%)}
.slide-arrow{top:108px}

/* services panel */
.services{left:76px;top:388px;width:751px;height:608px;background:var(--white);border-radius:0 0 8px 8px}
.section-tab{left:0;top:15px;width:188px;height:27px;background:var(--tab);color:var(--white);
  font-family:"Titillium Web",sans-serif;font-size:13px;line-height:27px;padding-left:32px;border-radius:0 4px 4px 0}
.service{width:195px}
.service h3{font-family:"Titillium Web",sans-serif;font-weight:400;font-size:13.5px;color:var(--heading);margin-bottom:4px}
.service .thumb{width:190px;height:89px;border:1px solid #c9c9c9;border-radius:3px;box-shadow:0 1px 3px rgba(0,0,0,.2)}
.service h4{font-family:"Titillium Web",sans-serif;font-weight:400;font-size:10.5px;line-height:14px;color:var(--sub);margin:8px 0 6px 4px;width:180px}
.service p{font-size:8.3px;line-height:13.6px;color:var(--body);margin-left:3px;width:188px}
.service p.placeholder{color:var(--muted)}
.service .more{position:absolute;left:4px;font-size:8px;color:var(--link);text-decoration:none}

/* footer */
.site-footer{left:0;top:1017px;width:902px;height:143px;background:var(--footer)}
.signup h3{font-family:"Titillium Web",sans-serif;font-weight:400;font-size:12.5px;color:#222}
.signup p{font-size:7.5px;line-height:13px;color:#222;width:180px;margin-top:6px}
.email{left:85px;top:79px;width:204px;height:19px;background:var(--white);font-size:7.5px;font-style:italic;color:#999;padding:5px 8px;
  box-shadow:0 6px 6px -4px rgba(0,0,0,.25)}
.subscribe{left:220px;top:107px;width:63px;height:20px;background:var(--navy-deep);color:var(--white);border-radius:3px;
  font-size:9px;font-weight:600;line-height:20px;text-align:center}
.link-col h4{font-family:"Titillium Web",sans-serif;font-weight:400;font-size:11px;color:#333;margin-bottom:5px}
.link-col ul{list-style:none}
.link-col li{font-size:8px;line-height:16px;color:#444;padding-left:12px;position:relative}
.link-col li::before{content:"›";position:absolute;left:1px;top:-1px;font-size:11px;color:#555}
.footer-bar{left:0;top:1160px;width:902px;height:40px;background:var(--footer-bar)}
.social{left:82px;top:10px;display:flex;gap:13px}
.social span{width:17px;height:17px;border-radius:2px;background:#5f7fa6}
.copyright{right:58px;top:8px;font-size:7.5px;color:#555;text-align:right;line-height:15px}
</style>
</head>
<body>

<header class="site-header abs">
  <svg width="902" height="108" viewBox="0 0 902 108">
    <path d="M0 70 C200 40 420 95 620 60 S850 40 902 55" fill="none" stroke="rgba(255,255,255,.35)" stroke-width="6"/>
    <path d="M0 85 C220 60 430 105 640 78 S860 62 902 72" fill="none" stroke="rgba(255,255,255,.5)" stroke-width="3"/>
  </svg>
  <div class="brand abs">
    <span class="brand-mark"></span>
    <span class="brand-name">Norvane</span>
  </div>
  <nav class="main-nav abs">
    <a href="#" style="width:67px">Home</a>
    <a href="#" style="width:66px">About Us</a>
    <a href="#" style="width:67px">Services</a>
    <a href="#" style="width:67px">Work</a>
    <a href="#" style="width:67px">Clients</a>
  </nav>
</header>

<section class="hero abs">
  <h1 class="hero-title abs">Graphic Design</h1>
  <p class="hero-text abs">Sed ut perspiciatis unde omnis iste natus error sit volupta-tem accusantium doloremque laudantium, totam rem aperiam, eaque ipsa quae ab illo inven tore veritatis et quasi</p>
  <div class="cta abs">CLICK HERE &gt;&gt;</div>
  <div class="cta-reflection abs"></div>
  <div class="hero-art abs" role="img" aria-label="Illustration of design tools: tablet, camera, pencils, printed flyers and software icons"></div>
  <svg class="slide-arrow abs" style="left:80px" width="24" height="36" viewBox="0 0 24 36"><path d="M18 4 L6 18 L18 32" fill="none" stroke="#fff" stroke-width="4"/></svg>
  <svg class="slide-arrow abs" style="left:780px" width="24" height="36" viewBox="0 0 24 36"><path d="M6 4 L18 18 L6 32" fill="none" stroke="#fff" stroke-width="4"/></svg>
</section>

<main class="services abs">
  <div class="section-tab abs">OUR SERVICES</div>

  <article class="service abs" style="left:32px;top:61px">
    <h3>Audio/Video Production</h3>
    <div class="thumb" role="img" aria-label="Photo of a film clapperboard and film reel" style="background:linear-gradient(135deg,#f2f2f2,#3a3a3a 60%,#888)"></div>
    <h4>We Don't Undervalue the Power of Sound</h4>
    <p>When something is lacking excellent audio it is the first thing the listener notices. Our highly experienced team understands what it takes to produce high quality sound whether it is an original score, musical arrangement, or a simple voiceover.</p>
    <a class="more" href="#" style="top:241px">View More &gt;&gt;</a>
  </article>

  <article class="service abs" style="left:273px;top:61px">
    <h3>Graphic Design</h3>
    <div class="thumb" role="img" aria-label="Sphere made of design words like flyer, logo and concept" style="background:radial-gradient(circle at 50% 70%,#e6e6e6,#ffffff 70%)"></div>
    <h4>Uenim ad minim veniam, quis nostrud laboris nisi</h4>
    <p class="placeholder">Uenim ad minim veniam, quis nostrud aboris nisi utaliquip ex irurdolor into Uenim ad minim veniam, quis nostrud aboris nisi utaliquip ex irurdolor into Uenim ad minim veniam, quis nostrud laboris nisi utaliquip ex irurdolor into</p>
    <a class="more" href="#" style="top:241px">View More &gt;&gt;</a>
  </article>

  <article class="service abs" style="left:514px;top:61px">
    <h3>Social Media</h3>
    <div class="thumb" role="img" aria-label="Colourful figures with speech bubbles" style="background:linear-gradient(90deg,#6cc24a,#d93a3a,#2f8fd6,#e84aa0,#2fb5c9,#f0a030)"></div>
    <h4>Create A Presence Everywhere</h4>
    <p>When executed correctly, social media can evolve your business. The Internet has brought about cutting-edge ways to interact, focus, and procure new customers. We realize it is stress-ful and time consuming to be able to keep up with social marketing.</p>
    <a class="more" href="#" style="top:241px">View More &gt;&gt;</a>
  </article>

  <article class="service abs" style="left:32px;top:347px">
    <h3>Web Development</h3>
    <div class="thumb" role="img" aria-label="Globe connected to people and computers in a network" style="background:radial-gradient(circle at 50% 45%,#3d8fd0,#bfe0f5 45%,#ffffff 75%)"></div>
    <h4>Uenim ad minim veniam, quis nostrud laboris nisi</h4>
    <p class="placeholder">Uenim ad minim veniam, quis nostrud aboris nisi utaliquip ex irurdolor into Uenim ad minim veniam, quis nostrud aboris nisi utaliquip ex irurdolor into Uenim ad minim veniam, quis nostrud laboris nisi utaliquip ex irurdolor into</p>
    <a class="more" href="#" style="top:233px">View More &gt;&gt;</a>
  </article>

  <article class="service abs" style="left:273px;top:347px">
    <h3>Apparel Design</h3>
    <div class="thumb" role="img" aria-label="Hand with pen beside rows of website layouts" style="background:linear-gradient(90deg,#f4f4f4 30%,#c8c8c8 60%,#e8e8e8)"></div>
    <h4>Dress to Impress</h4>
    <p>Being one of the most powerful tools for enhancing your companies image, your web-site needs to be impeccable. Many times, your website will be a person's first interaction with your company. Visitors will form an opinion as soon as they hit your home page.</p>
    <a class="more" href="#" style="top:232px">View More &gt;&gt;</a>
  </article>

  <article class="service abs" style="left:522px;top:347px">
    <h3>Photography</h3>
    <div class="thumb" role="img" aria-label="Row of colourful rubber ducks on a reflective surface" style="background:linear-gradient(90deg,#2b6fc4,#e8449a 40%,#f05a3a 65%,#f2c21c);opacity:.85"></div>
    <h4>Exquisite, Memorable Images</h4>
    <p>We recognize what stands out when it comes to framing a photo. Whether it is a wedding or the opening of your new restaurant, a flower arrangement or your portrait, you can be sure your photos will not be forgotten. With our knowledge, cameras.</p>
    <a class="more" href="#" style="top:232px">View More &gt;&gt;</a>
  </article>
</main>

<footer class="site-footer abs">
  <div class="signup abs" style="left:86px;top:21px">
    <h3>Sign Up to Stay in Touch</h3>
    <p>Please enter your email address below to sign up for our mailing list.</p>
  </div>
  <div class="email abs">your email address here..</div>
  <div class="subscribe abs">Subscribe ›</div>

  <div class="link-col abs" style="left:402px;top:14px">
    <h4>PRODUCTS</h4>
    <ul><li>Nunc varius eros</li><li>Sed velit quis</li><li>arcu orne laoreet.</li><li>Curabitur luctus</li><li>Intege ornare</li></ul>
  </div>
  <div class="link-col abs" style="left:553px;top:14px">
    <h4>SUPPORT</h4>
    <ul><li>Nunc varius eros</li><li>Sed velit quis</li><li>arcu orne laoreet.</li><li>Curabitur luctus</li><li>Intege ornare</li></ul>
  </div>
  <div class="link-col abs" style="left:704px;top:14px">
    <h4>SERVICES</h4>
    <ul><li>Nunc varius eros</li><li>Sed velit quis</li><li>arcu orne laoreet.</li><li>Curabitur luctus</li><li>Intege ornare</li></ul>
  </div>
</footer>

<div class="footer-bar abs">
  <div class="social abs"><span></span><span></span><span></span><span></span><span></span></div>
  <div class="copyright abs">© 2013 Norvane. &nbsp; All right reserved<br>x2</div>
</div>

</body>
</html>
```